Birchline Pencil Portraits

Attempting to reach a consumer interested in affordable art to give as gifts, or to keep for themselves. Drawings to focus on beloved objects: homes, boats, cars...or loved personal photographs of...pets, friends and family. Attempting to reach customers with disposable income that may have not considered hand drawn art due to preconceived notions of cost/risk. The drawings would be guaranteed with payment due after seeing the finished product. No risk and all reward.

Target Market(s)

Adults with disposable income. New home/apartment buyers looking to decorate. People with treasured photographs. Sentimental personalities. Creative gift givers.

Industry/Entity Type

Consumer

Contact Information for Business Card

A photograph of a log cabin and on the flip-side a drawing of that photograph.

Font styles to use
Serif
Sans Serif

Requirements
Must have
• Contact information.
• Photograph w/drawing

```html
<!DOCTYPE html>
<html lang="en">
<head>
<meta charset="utf-8">
<title>Birchline Pencil Portraits – Business Card</title>
<link href="https://fonts.googleapis.com/css2?family=Great+Vibes&family=Questrial&family=Mulish:wght@700&display=swap" rel="stylesheet">
<style>
  :root {
    --page: #ffffff;
    --parchment-light: #efe6d2;
    --parchment-mid: #ddcdaa;
    --parchment-deep: #b49a72;
    --parchment-edge: #5a4636;
    --ink: #2b2623;
    --photo-frame: #ffffff;
    --lawn: #4f9a2c;
    --roof: #5f6470;
    --logs: #a9865a;
    --foliage: #8fae5a;
    --sky: #dfe8d6;
    --drawn-roof: #7b6f9c;
    --drawn-lawn: #7dbb3c;
  }
  * { box-sizing: border-box; margin: 0; padding: 0; }
  html, body { width: 949px; height: 1200px; overflow: hidden; background: var(--page); }
  .canvas { position: relative; width: 949px; height: 1200px; }

  .card {
    position: absolute;
    overflow: hidden;
    background:
      radial-gradient(ellipse at 50% 45%, var(--parchment-light) 0%, var(--parchment-mid) 62%, var(--parchment-deep) 90%, var(--parchment-edge) 100%);
    box-shadow: 4px 10px 14px rgba(0,0,0,0.28), inset 0 0 0 2px rgba(70,50,40,0.55);
  }
  .card--front { left: 93px; top: 112px; width: 737px; height: 454px; }
  .card--back  { left: 88px; top: 628px; width: 739px; height: 455px; }

  .script {
    position: absolute;
    font-family: "Great Vibes", cursive;
    color: var(--ink);
    white-space: nowrap;
    line-height: 1;
  }
  .business-name { font-weight: 400; }
  .front-title { left: 383px; top: 98px; font-size: 31px; }
  .tagline { font-size: 33px; }
  .tagline--first { left: 44px; top: 305px; }
  .tagline--second { left: 142px; top: 350px; }

  .photo {
    position: absolute;
    left: 22px; top: 24px;
    width: 338px; height: 242px;
    padding: 7px;
    background: var(--photo-frame);
    transform: rotate(-4deg);
    box-shadow: 2px 4px 8px rgba(0,0,0,0.3);
    z-index: 2;
  }
  .photo__image {
    width: 100%; height: 100%;
    background: linear-gradient(180deg, var(--sky) 0%, var(--roof) 22%, var(--logs) 45%, var(--foliage) 62%, var(--lawn) 78%, #3f8424 100%);
  }
  .drawing {
    position: absolute;
    left: 357px; top: 158px;
    width: 368px; height: 268px;
    transform: rotate(3deg);
    background: linear-gradient(180deg, #e8dcc0 0%, var(--drawn-roof) 22%, #c49a62 46%, #8fb35a 64%, var(--drawn-lawn) 80%, #6aa833 100%);
    box-shadow: 2px 4px 8px rgba(0,0,0,0.25);
    z-index: 1;
  }

  .back-drawing {
    position: absolute; inset: 0;
    background: linear-gradient(180deg, rgba(230,220,190,0.15) 0%, rgba(150,140,150,0.3) 25%, rgba(200,175,130,0.3) 50%, rgba(170,190,110,0.3) 72%, rgba(160,200,90,0.4) 100%);
  }
  .back-title { left: 60px; top: 108px; font-size: 36px; }
  .contact {
    position: absolute; left: 100px; top: 189px;
    font-family: "Questrial", "Century Gothic", sans-serif;
    color: var(--ink);
    list-style: none;
  }
  .contact__name {
    font-family: "Mulish", "Century Gothic", sans-serif;
    font-weight: 700; font-size: 19px; height: 26px; margin-bottom: 12px;
  }
  .contact__line { display: flex; align-items: center; gap: 8px; font-size: 21px; height: 41px; }
  .contact__icon { width: 20px; height: 20px; flex: none; }
</style>
</head>
<body>
<div class="canvas">

  <section class="card card--front" aria-label="Card front">
    <div class="photo"><div class="photo__image" role="img" aria-label="Photograph of a log cabin among trees on a green lawn"></div></div>
    <div class="drawing" role="img" aria-label="Hand drawn coloured pencil rendering of the same log cabin"></div>
    <p class="script business-name front-title">Birchline Pencil Portraits</p>
    <p class="script tagline tagline--first">Homes, boats, pets,</p>
    <p class="script tagline tagline--second">friends... and more</p>
  </section>

  <section class="card card--back" aria-label="Card back">
    <div class="back-drawing" role="img" aria-label="Faded hand drawn log cabin scene as background"></div>
    <p class="script business-name back-title">Birchline Pencil Portraits</p>
    <ul class="contact">
      <li class="contact__name">Martin Ellery</li>
      <li class="contact__line">
        <svg class="contact__icon" viewBox="0 0 24 24" aria-hidden="true"><path d="M7 3l3 4-2 2c1 3 3 5 6 6l2-2 4 3-2 4C10 20 4 14 3 5z" fill="none" stroke="#2b2623" stroke-width="2" stroke-linejoin="round"/></svg>
        248 555 0143
      </li>
      <li class="contact__line">
        <svg class="contact__icon" viewBox="0 0 24 24" aria-hidden="true"><rect x="2" y="6" width="20" height="13" fill="none" stroke="#2b2623" stroke-width="2"/><path d="M2 6l10 8 10-8" fill="none" stroke="#2b2623" stroke-width="2"/></svg>
        Martinellery@example.com
      </li>
      <li class="contact__line">
        <svg class="contact__icon" viewBox="0 0 24 24" aria-hidden="true"><path d="M2 11L12 4l10 7z" fill="#2b2623"/><rect x="4" y="11" width="16" height="9" fill="#2b2623"/><rect x="10" y="14" width="4" height="6" fill="#efe6d2"/></svg>
        112 N Birchwood rd, lake ridge, mi 49000
      </li>
    </ul>
  </section>

</div>
</body>
</html>
```